Velmora Business Card

We need a design for business cards for our new company. We are a resident safety and security company company that focuses on senior living communities. we provide Nurse call, Access control, CCTV, Wired and wireless network infrastructure, Wander Management, and much more!

Our logo is the circuit board shield. Representing our high tech security solutions. I would like the business card to bring the same theme with perhaps some circuit board traces around the card similar to our logo

```html
<!DOCTYPE html>
<html lang="en">
<head>
<meta charset="utf-8">
<title>Velmora Business Card</title>
<link rel="stylesheet" href="https://fonts.googleapis.com/css2?family=Libre+Baskerville:wght@400;700&family=Montserrat:wght@400;500&display=swap">
<style>
  :root {
    --stage: #3a3a3c;
    --blue-deep: #2c58b2;
    --blue-mid: #2f7fcf;
    --blue-light: #37b9ec;
    --ink-blue: #2a4fae;
    --ink-grey: #3b3b3f;
    --white: #ffffff;
    --card-w: 540px;
    --card-h: 310px;
  }
  * { box-sizing: border-box; margin: 0; padding: 0; }
  html, body { width: 1200px; height: 875px; overflow: hidden; }
  body {
    background: var(--stage);
    display: flex;
    align-items: center;
    justify-content: center;
    gap: 40px;
  }
  .card {
    position: relative;
    width: var(--card-w);
    height: var(--card-h);
    border-radius: 16px;
    overflow: hidden;
    box-shadow: 0 18px 40px rgba(0,0,0,.45);
  }

  /* Front */
  .card-front {
    background: linear-gradient(30deg, var(--blue-light) 0%, var(--blue-mid) 45%, var(--blue-deep) 100%);
  }
  .trace-field {
    position: absolute; inset: 0;
    background: radial-gradient(ellipse at 60% 40%, rgba(255,255,255,.08), rgba(255,255,255,0) 70%);
  }
  .front-wordmark {
    position: absolute;
    left: 0; right: 0; top: 50%;
    transform: translateY(-50%);
    text-align: center;
    font-family: "Libre Baskerville", serif;
    font-weight: 400;
    font-size: 52px;
    letter-spacing: 3px;
    color: var(--white);
    text-transform: uppercase;
  }

  /* Back */
  .card-back { background: var(--white); }
  .back-sweep { position: absolute; inset: 0; }
  .back-wordmark {
    position: absolute;
    right: 40px; top: 120px;
    width: 200px;
    text-align: center;
    font-family: "Libre Baskerville", serif;
    font-size: 30px;
    letter-spacing: 2px;
    color: var(--white);
    text-transform: uppercase;
  }
  .name-tab {
    position: absolute;
    left: 0; top: 96px;
    width: 12px; height: 40px;
    background: var(--ink-blue);
  }
  .identity { position: absolute; left: 34px; top: 92px; }
  .person-name {
    font-family: "Libre Baskerville", serif;
    font-weight: 700;
    font-size: 21px;
    color: var(--ink-blue);
    letter-spacing: .5px;
  }
  .person-role {
    font-family: "Montserrat", sans-serif;
    font-size: 12.5px;
    color: var(--ink-grey);
    margin-top: 2px;
  }
  .contact {
    position: absolute;
    left: 90px; top: 188px;
    font-family: "Montserrat", sans-serif;
    font-size: 12px;
    line-height: 17px;
    color: var(--ink-grey);
    list-style: none;
  }
  .address { margin-bottom: 8px; }
  .contact-line { display: flex; align-items: center; gap: 8px; }
  .contact-line svg { width: 11px; height: 11px; fill: var(--ink-blue); flex: none; }
  .web-domain { color: var(--ink-blue); }
</style>
</head>
<body>

  <section class="card card-front">
    <div class="trace-field" role="img" aria-label="Faint circuit board trace pattern across the card"></div>
    <div class="front-wordmark">Velmora</div>
  </section>

  <section class="card card-back">
    <svg class="back-sweep" viewBox="0 0 540 310" preserveAspectRatio="none" aria-hidden="true">
      <defs>
        <linearGradient id="sweepFill" x1="0" y1="1" x2="1" y2="0">
          <stop offset="0" stop-color="#37b9ec"/>
          <stop offset=".5" stop-color="#2f7fcf"/>
          <stop offset="1" stop-color="#2c58b2"/>
        </linearGradient>
      </defs>
      <path d="M270 0 H540 V310 H500 C505 250 520 170 470 100 C430 40 360 20 270 0 Z" fill="url(#sweepFill)"/>
      <path d="M300 80 C330 30 400 18 480 22 C520 90 520 200 460 260 C420 300 340 290 300 240 C260 190 270 130 300 80 Z" fill="url(#sweepFill)"/>
    </svg>
    <div class="back-wordmark">Velmora</div>

    <div class="name-tab"></div>
    <div class="identity">
      <div class="person-name">DORIAN HALE</div>
      <div class="person-role">CEO/Founder</div>
    </div>

    <ul class="contact">
      <li class="address">48 Larkfield Ave Ste B<br>Northvale, AB 204817</li>
      <li class="contact-line">
        <svg viewBox="0 0 24 24"><path d="M6.6 10.8a15.2 15.2 0 0 0 6.6 6.6l2.2-2.2a1 1 0 0 1 1-.25 11.4 11.4 0 0 0 3.6.57 1 1 0 0 1 1 1V20a1 1 0 0 1-1 1A17 17 0 0 1 3 4a1 1 0 0 1 1-1h3.5a1 1 0 0 1 1 1c0 1.25.2 2.45.57 3.57a1 1 0 0 1-.25 1z"/></svg>
        +823-410-2287
      </li>
      <li class="contact-line">
        <svg viewBox="0 0 24 24"><path d="M2 5h20v14H2z M2 5l10 8 10-8" stroke="#fff" stroke-width="1.5"/></svg>
        d.hale@velmoraLLC.com
      </li>
      <li class="contact-line">
        <svg viewBox="0 0 24 24"><circle cx="12" cy="12" r="10"/><path d="M2 12h20M12 2c3 3 3 17 0 20M12 2c-3 3-3 17 0 20" stroke="#fff" stroke-width="1.4" fill="none"/></svg>
        <span>www.<span class="web-domain">velmoraLLC</span>.com</span>
      </li>
    </ul>
  </section>

</body>
</html>
```